Dunmore Plumbing LLC business card

Would like a modern looking business card with my new logo

Contact Information for Business Card

Calvin Dunmore 2418 Elm Hollow Rd Brackenford, KT 06999, Dunmoreplumbingllc@exampletrade.com, 203-555-0174

```html
<!DOCTYPE html>
<html lang="en">
<head>
<meta charset="utf-8">
<title>Dunmore Plumbing LLC – Business Card</title>
<link href="https://fonts.googleapis.com/css2?family=Roboto:wght@400;700;900&family=Saira:wght@800&display=swap" rel="stylesheet">
<style>
  :root {
    --page: #2c2c2c;
    --card: #232325;
    --card-edge: #1e1e20;
    --blue: #0b9ad6;
    --silver: #a9aaad;
    --emboss: #3e3f42;
    --white: #f2f2f2;
    --ink: #16181a;
  }
  * { margin: 0; padding: 0; box-sizing: border-box; }
  html, body { width: 1200px; height: 1138px; overflow: hidden; background: var(--page); }
  body { position: relative; font-family: "Roboto", sans-serif; }

  .card {
    position: absolute;
    border-radius: 14px;
    overflow: hidden;
    background: linear-gradient(160deg, #262628 0%, var(--card) 60%, var(--card-edge) 100%);
  }
  .card--front { left: 272px; top: 184px; width: 622px; height: 376px; }
  .card--back  { left: 274px; top: 606px; width: 619px; height: 375px; }

  /* front */
  .front-name {
    position: absolute; left: 0; right: 0; top: 125px;
    text-align: center; color: var(--emboss);
    font-family: "Roboto", sans-serif; font-weight: 900;
    line-height: 1;
  }
  .front-name__main { display: block; font-size: 70px; letter-spacing: 4px; }
  .front-name__sub  { display: block; font-size: 24px; letter-spacing: 6px; margin-top: 10px; }
  .front-tagline {
    position: absolute; left: 0; right: 0; top: 326px;
    display: flex; justify-content: center; align-items: center; gap: 24px;
    color: #e6e6e6; font-size: 17px;
  }
  .front-tagline__rule { width: 70px; height: 2px; background: var(--blue); }

  /* back */
  .back-name {
    position: absolute; left: 26px; top: 72px; width: 290px;
    color: var(--white); font-weight: 900; line-height: 1;
  }
  .back-name__main { display: block; font-size: 44px; letter-spacing: 1px; }
  .back-name__sub  { display: block; font-size: 17px; letter-spacing: 3px; margin-top: 8px; }
  .holder { position: absolute; right: 27px; top: 76px; text-align: right; }
  .holder__name {
    font-family: "Saira", sans-serif; font-weight: 800;
    color: var(--blue); font-size: 27px; line-height: 1; letter-spacing: 0.5px;
  }
  .holder__title { color: var(--white); font-size: 17px; margin-top: 4px; }
  .address {
    position: absolute; left: 53px; width: 220px; top: 200px;
    text-align: center; color: var(--white); font-size: 17px; line-height: 24px;
    font-style: normal;
  }
  .waves { position: absolute; left: 0; top: 0; width: 619px; height: 375px; }
  .contact {
    position: absolute; right: 28px; top: 294px;
    color: var(--ink); font-size: 17px; line-height: 25px; text-align: right;
  }
  .contact__row { display: flex; justify-content: flex-end; align-items: center; gap: 14px; }
  .contact__icon { width: 16px; height: 14px; }
</style>
</head>
<body>

<section class="card card--front">
  <div class="front-name">
    <span class="front-name__main">DUNMORE</span>
    <span class="front-name__sub">PLUMBING LLC</span>
  </div>
  <div class="front-tagline">
    <span class="front-tagline__rule"></span>
    <span>Dunmore Plumbing LLC</span>
    <span class="front-tagline__rule"></span>
  </div>
</section>

<section class="card card--back">
  <svg class="waves" viewBox="0 0 619 375" aria-hidden="true">
    <path d="M0 262 C120 330 250 322 380 270 C470 234 540 204 619 228 L619 246 C540 222 470 250 380 287 C250 338 120 342 0 286 Z" fill="var(--silver)"/>
    <path d="M40 262 C140 306 250 304 330 290" stroke="var(--silver)" stroke-width="2" fill="none"/>
    <path d="M0 302 C120 350 260 334 390 280 C470 248 540 230 619 252 L619 375 L0 375 Z" fill="var(--blue)"/>
  </svg>

  <div class="back-name">
    <span class="back-name__main">DUNMORE</span>
    <span class="back-name__sub">PLUMBING LLC</span>
  </div>

  <div class="holder">
    <div class="holder__name">CALVIN DUNMORE</div>
    <div class="holder__title">Managing Director</div>
  </div>

  <address class="address">
    2418 Elm Hollow Rd<br>Brackenford, KT 06999
  </address>

  <div class="contact">
    <div class="contact__row">
      <span>203-555-0174</span>
      <svg class="contact__icon" viewBox="0 0 16 14" aria-hidden="true">
        <path d="M1 5 C1 1 15 1 15 5 L11 5 L11 3 L5 3 L5 5 Z" fill="var(--ink)"/>
        <path d="M4 6 L12 6 L15 13 L1 13 Z" fill="var(--ink)"/>
        <circle cx="8" cy="9.5" r="1.8" fill="var(--blue)"/>
      </svg>
    </div>
    <div class="contact__row">
      <span>Dunmoreplumbingllc@exampletrade.com</span>
      <svg class="contact__icon" viewBox="0 0 16 14" aria-hidden="true">
        <rect x="1" y="2" width="14" height="10" fill="var(--ink)"/>
        <path d="M1 2 L8 8 L15 2 M1 12 L6 7 M15 12 L10 7" stroke="var(--blue)" stroke-width="1" fill="none"/>
      </svg>
    </div>
  </div>
</section>

</body>
</html>
```